Business Card Design Project

I am opening a skin care studio called Glow Bloom by Marisa. I will be offering a wide range of unique and affordable skin services including facials, chemical peels, microdermabrasion treatments, body wraps, salt glows, all waxing and eye lash extensions. If the business cards depicts what I would like, this would lead to brochures, web design, signs, etc.
Updates

Project Deadline Extended
Reason: A request to extend deadline was requested. I will be more than happy to accommodate.

Industry/Entity Type

Business

Requirements
Nice to have
• facial features so prospective client clearly identifies what type of business this is. Not stuffy or boring "spa" looking graphics. I am focusing just on face, body, waxing, eyelashes. No massage or nails.

```html
<!DOCTYPE html>
<html lang="en">
<head>
<meta charset="utf-8">
<title>Glow Bloom by Marisa – Business Cards</title>
<link rel="stylesheet" href="https://fonts.googleapis.com/css2?family=Questrial&display=swap">
<style>
  :root {
    --page-bg: #e9e9ec;
    --card-white: #ffffff;
    --card-grey: #f1f1f2;
    --ink: #3b3d47;
    --brand: #4f5fb3;
    --tint-light: #dfe3f4;
    --tint-deep: #5a6bbd;
  }
  * { box-sizing: border-box; margin: 0; padding: 0; }
  html, body { width: 1200px; height: 880px; overflow: hidden; }
  body {
    background: var(--page-bg);
    font-family: "Questrial", "Century Gothic", sans-serif;
    color: var(--ink);
    position: relative;
  }
  .card {
    position: absolute;
    top: 125px;
    width: 360px;
    height: 630px;
    overflow: hidden;
    box-shadow: 0 6px 22px rgba(0,0,0,0.18);
  }
  .card--back { left: 170px; background: var(--card-grey); }
  .card--front { left: 670px; background: var(--card-white); }

  .card__decor { position: absolute; }
  .card--back .card__decor {
    left: 0; right: 0; bottom: 0;
    height: 170px;
    background: linear-gradient(160deg, rgba(241,241,242,0) 35%, var(--tint-light) 60%, var(--tint-deep) 100%);
  }
  .card--front .card__decor {
    left: 0; right: 0; bottom: 0;
    height: 250px;
    background: linear-gradient(180deg, rgba(255,255,255,0) 0%, var(--tint-light) 30%, var(--tint-deep) 100%);
  }

  .brand-name {
    position: absolute;
    right: 34px;
    top: 70px;
    text-align: right;
    color: var(--brand);
    font-weight: 400;
    line-height: 1;
  }
  .brand-name__main { display: block; font-size: 38px; }
  .brand-name__sub { display: block; font-size: 21px; margin-top: 6px; }

  .service-list {
    position: absolute;
    left: 40px;
    top: 240px;
    list-style: none;
    font-size: 15px;
    line-height: 1.75;
  }
  .service-list li span { margin-right: 12px; white-space: nowrap; }
  .service-list li span::before {
    content: "";
    display: inline-block;
    width: 5px; height: 5px;
    border-radius: 50%;
    background: var(--brand);
    margin-right: 6px;
    vertical-align: middle;
  }
  .contact-list {
    position: absolute;
    left: 112px;
    top: 245px;
    list-style: none;
    font-size: 14px;
    line-height: 1.9;
  }
  .contact-list .label { color: var(--brand); margin-right: 4px; }
</style>
</head>
<body>

  <section class="card card--back" aria-label="Card back with contact details">
    <div class="card__decor" role="img" aria-label="Soft blue curved band decoration in the lower corner"></div>
    <h1 class="brand-name">
      <span class="brand-name__main">Glow Bloom</span>
      <span class="brand-name__sub">by Marisa</span>
    </h1>
    <ul class="contact-list">
      <li><span class="label">p:</span>555.214.3380</li>
      <li><span class="label">f:</span>555.214.3381</li>
      <li><span class="label">e:</span>hello@glowbloomstudio.com</li>
      <li><span class="label">w:</span>www.glowbloomstudio.com</li>
    </ul>
  </section>

  <section class="card card--front" aria-label="Card front with services">
    <div class="card__decor" role="img" aria-label="Soft blue layered curve decoration across the lower card"></div>
    <h2 class="brand-name">
      <span class="brand-name__main">Glow Bloom</span>
      <span class="brand-name__sub">by Marisa</span>
    </h2>
    <ul class="service-list">
      <li><span>facials</span><span>chemical peels</span></li>
      <li><span>microdermabrasion treatments</span></li>
      <li><span>body wraps</span><span>salt glows</span></li>
      <li><span>all waxing</span><span>eye lash extensions</span></li>
    </ul>
  </section>

</body>
</html>
```